Natural Light/Organic/Documentary Photography Business

I like a simple, approachable, feminine, earthy/organic feel. Earth/neutral tones, nothing too loud or obnoxious. I like the watercolor look. I don't want anything too trendy or something I'll get tired of after a couple months. As far as colors, I am much more a fan of cream/taupe/blue/green...not a fan of pink or purple at all.

Target Market(s)

Weddings & Families

Industry/Entity Type

Wedding Photography

Contact Information for Business Card

website, email, phone number

Font styles to use
Other font styles liked:
• Horizontes, Gotham

Colors

Designer to choose colors to be used in the design.

Requirements
Must have
• Website: www.elspethmarlowe.com
• Phone: 412.638.9057
• Email: elspeth@elspethmarlowe.com
Nice to have
• I like the watercolor look but its not necessary. I like simple/earthy tones. Nothing too loud or distracting. Simple & feminine without being too girly. I like an approachable/soft feel.
• Instagram: www.instagram.com/elspethmarlowephotography/
Should not have
• NO loud colors or design or pattern. I do not want a photo of a camera or lens or anything cheesy like that.

```html
<!DOCTYPE html>
<html lang="en">
<head>
<meta charset="utf-8">
<title>Elspeth Marlowe Photography — Business Card</title>
<link rel="stylesheet" href="https://fonts.googleapis.com/css2?family=Questrial&display=swap">
<style>
  :root {
    --canvas-bg: #ecebe8;
    --card-paper: #ffffff;
    --ink: #1b1b1b;
    --aqua-light: #1fe0dc;
    --aqua-mid: #17cfca;
    --teal-light: #22cdb8;
    --teal-deep: #1db596;
    --card-shadow: rgba(40, 40, 40, 0.18);
  }
  * { margin: 0; padding: 0; box-sizing: border-box; }
  html, body {
    width: 1200px;
    height: 1200px;
    overflow: hidden;
    background: var(--canvas-bg);
    font-family: "Questrial", "Century Gothic", sans-serif;
    color: var(--ink);
  }
  .canvas {
    position: relative;
    width: 1200px;
    height: 1200px;
  }
  .card {
    position: absolute;
    left: 180px;
    width: 840px;
    height: 480px;
    background: var(--card-paper);
    box-shadow: 0 10px 30px var(--card-shadow);
    overflow: hidden;
  }
  .card--front { top: 90px; }
  .card--back { top: 630px; }
  .card__wash {
    position: absolute;
    inset: 0;
    width: 840px;
    height: 480px;
  }
  .brand-name {
    position: absolute;
    left: 0;
    right: 0;
    top: 208px;
    text-align: center;
    font-size: 58px;
    letter-spacing: 3px;
    color: var(--ink);
  }
  .contact-line {
    position: absolute;
    left: 0;
    right: 0;
    text-align: center;
    color: var(--ink);
  }
  .contact-line--phone { top: 150px; font-size: 30px; letter-spacing: 2px; }
  .contact-line--email { top: 278px; font-size: 30px; letter-spacing: 1px; }
  .contact-line--web { top: 392px; font-size: 22px; letter-spacing: 1px; }
  .contact-icon {
    position: absolute;
    left: 50%;
    transform: translateX(-50%);
    fill: var(--ink);
  }
  .contact-icon--phone { top: 100px; width: 38px; height: 34px; }
  .contact-icon--mail { top: 232px; width: 38px; height: 30px; }
</style>
</head>
<body>
<main class="canvas">

  <section class="card card--front" aria-label="Business card front">
    <svg class="card__wash" viewBox="0 0 840 480" role="img" aria-label="Aqua and teal watercolour brush strokes">
      <defs>
        <linearGradient id="wash-aqua" x1="0" y1="0" x2="0" y2="1">
          <stop offset="0" stop-color="var(--aqua-light)"/>
          <stop offset="1" stop-color="var(--aqua-mid)"/>
        </linearGradient>
        <linearGradient id="wash-teal" x1="0" y1="0" x2="0" y2="1">
          <stop offset="0" stop-color="var(--teal-light)"/>
          <stop offset="1" stop-color="var(--teal-deep)"/>
        </linearGradient>
      </defs>
      <path fill="url(#wash-aqua)" d="M120 140 Q300 120 520 128 Q660 132 770 150 L752 170 L780 186 L748 204 L774 222 L740 246 Q560 252 360 250 Q220 248 118 244 Q100 200 120 140 Z"/>
      <path fill="url(#wash-teal)" opacity="0.95" d="M96 232 Q280 224 480 230 Q640 236 760 246 L740 268 L770 290 L736 312 L756 336 L720 350 Q520 358 320 352 Q180 348 110 340 Q86 290 96 232 Z"/>
    </svg>
    <p class="brand-name">Elspeth Marlowe</p>
  </section>

  <section class="card card--back" aria-label="Business card back">
    <svg class="card__wash" viewBox="0 0 840 480" role="img" aria-label="Aqua and teal watercolour brush strokes">
      <defs>
        <linearGradient id="wash-aqua-back" x1="0" y1="0" x2="0" y2="1">
          <stop offset="0" stop-color="var(--aqua-light)"/>
          <stop offset="1" stop-color="var(--aqua-mid)"/>
        </linearGradient>
        <linearGradient id="wash-teal-back" x1="0" y1="0" x2="0" y2="1">
          <stop offset="0" stop-color="var(--teal-light)"/>
          <stop offset="1" stop-color="var(--teal-deep)"/>
        </linearGradient>
      </defs>
      <path fill="url(#wash-aqua-back)" d="M128 80 Q320 64 540 70 Q680 74 770 90 L752 110 L782 128 L750 148 L772 168 L738 200 Q560 208 360 206 Q220 204 124 198 Q104 140 128 80 Z"/>
      <path fill="url(#wash-teal-back)" opacity="0.95" d="M96 210 Q280 200 480 206 Q640 212 770 220 L748 244 L778 268 L744 292 L764 318 L726 334 Q520 342 320 338 Q180 334 108 326 Q84 270 96 210 Z"/>
    </svg>

    <svg class="contact-icon contact-icon--phone" viewBox="0 0 38 34" aria-hidden="true">
      <path d="M2 9 Q19 -2 36 9 L33 15 L27 13 L26 9 Q19 6 12 9 L11 13 L5 15 Z"/>
      <path d="M10 14 L28 14 L34 30 Q34 33 31 33 L7 33 Q4 33 4 30 Z"/>
      <circle cx="19" cy="24" r="5" fill="#ffffff" opacity="0.0"/>
    </svg>
    <p class="contact-line contact-line--phone">412.638.9057</p>

    <svg class="contact-icon contact-icon--mail" viewBox="0 0 38 30" aria-hidden="true">
      <path d="M1 10 L19 1 L37 10 L37 29 L1 29 Z"/>
      <path d="M3 12 L19 22 L35 12" fill="none" stroke="#1fd0bc" stroke-width="2"/>
    </svg>
    <p class="contact-line contact-line--email">elspeth@elspethmarlowe.com</p>

    <p class="contact-line contact-line--web">www.elspethmarlowe.com</p>
  </section>

</main>
</body>
</html>
```